Business Card Design Project

Business card design for an IT Service company. A logo has already been created in a different contest and has been attached to this project. Ideally we're looking for a double sided business card that matches the look and feel of our newly created logo.

We're open to creativity if you feel a tag line is needed such as "IT Services and Application Development". We're open to really and look and feel - even single sided business cards if you feel you have something that's a great idea.

Last thought here - I'm not sure how it'll look but maybe a two tone card? One side dark blue and the other side white? Don't limit the design submissions to this tho - just curious if it would look good

Nothing too busy please - simple... Thank you and happy designing!

Target Market(s)

Businesses that require IT Services and support for hosted services, technical consultation, web design.

Industry/Entity Type

Business

Font styles to use
Sans Serif

Requirements
Must have
• Use the colors provided in the logo (see attachment) or additional colors that compliment
Must have the following contact info (not necessarily in this order):
- Owen Marsh
- Founding Partner
- omarsh@velomarquin.com
- 555-271-3948
- www.velomarquin.com

```html
<!DOCTYPE html>
<html lang="en">
<head>
<meta charset="utf-8">
<title>VeloMarquin Business Card</title>
<link href="https://fonts.googleapis.com/css2?family=Open+Sans:wght@400;600;700&display=swap" rel="stylesheet">
<style>
  :root {
    --stage: #646464;
    --card-top: #f1f1f0;
    --card-bottom: #f8f8f8;
    --navy: #262b3a;
    --green: #5f8a2a;
    --ink: #2a2d36;
    --white: #ffffff;
  }
  * { margin: 0; padding: 0; box-sizing: border-box; }
  html, body {
    width: 1200px; height: 1200px; overflow: hidden;
    background: var(--stage);
    font-family: "Open Sans", Arial, sans-serif;
  }
  .card {
    position: absolute; left: 115px; width: 969px; height: 580px;
    background: linear-gradient(to bottom, var(--card-top), var(--card-bottom));
    overflow: hidden;
  }
  .card--front { top: 13px; }
  .card--back { top: 607px; }

  /* front */
  .brand-lockup {
    position: absolute; left: 0; right: 0; top: 228px;
    display: flex; flex-direction: column; align-items: center;
  }
  .brand-row { display: flex; align-items: center; gap: 18px; }
  .brand-square { width: 64px; height: 64px; background: var(--navy); }
  .brand-name {
    font-weight: 700; color: var(--navy);
    font-size: 82px; line-height: 1; letter-spacing: -1px;
  }
  .brand-tagline {
    margin-top: 14px; color: var(--green); font-weight: 600;
    font-size: 18px; letter-spacing: 2.6px; text-transform: uppercase;
  }

  /* back */
  .band { position: absolute; top: 246px; height: 91px; background: var(--navy); }
  .band--left { left: 0; width: 65px; }
  .band--right { left: 484px; right: 0; padding: 24px 0 0 33px; color: var(--white); }
  .person-name { font-size: 29px; font-weight: 400; letter-spacing: 1px; line-height: 1; }
  .person-role { margin-top: 8px; font-size: 18px; line-height: 1; }

  .brand-lockup--small { left: 85px; right: auto; top: 270px; align-items: flex-start; }
  .brand-lockup--small .brand-square { width: 40px; height: 40px; }
  .brand-lockup--small .brand-row { gap: 12px; }
  .brand-lockup--small .brand-name { font-size: 52px; }
  .brand-lockup--small .brand-tagline { margin-top: 8px; font-size: 13px; letter-spacing: 1.6px; }

  .contact { position: absolute; top: 385px; display: grid; row-gap: 8px; }
  .contact--left { right: 510px; }
  .contact--right { left: 481px; }
  .contact-line {
    display: flex; align-items: center; gap: 11px;
    font-size: 18px; color: var(--ink); height: 27px;
  }
  .contact--left .contact-line { justify-content: flex-end; }
  .icon { width: 27px; height: 27px; background: var(--green); display: block; flex: none; }
</style>
</head>
<body>

<section class="card card--front">
  <div class="brand-lockup">
    <div class="brand-row">
      <span class="brand-square"></span>
      <span class="brand-name">VeloMarquin</span>
    </div>
    <div class="brand-tagline">IT Services and Application Management</div>
  </div>
</section>

<section class="card card--back">
  <div class="band band--left"></div>
  <div class="band band--right">
    <div class="person-name">OWEN MARSH</div>
    <div class="person-role">Founding Partner</div>
  </div>

  <div class="brand-lockup brand-lockup--small">
    <div class="brand-row">
      <span class="brand-square"></span>
      <span class="brand-name">VeloMarquin</span>
    </div>
    <div class="brand-tagline">IT Services and Application Management</div>
  </div>

  <div class="contact contact--left">
    <div class="contact-line">
      <span>48/B, Harbor Lane, Mill Street, Town</span>
      <svg class="icon" viewBox="0 0 27 27" aria-hidden="true">
        <rect width="27" height="27" fill="#5f8a2a"/>
        <path d="M10 6 L17 13.5 L10 21" fill="none" stroke="#fff" stroke-width="4"/>
      </svg>
    </div>
    <div class="contact-line">
      <span>555-271-3948 / 555-271-3950</span>
      <svg class="icon" viewBox="0 0 27 27" aria-hidden="true">
        <rect width="27" height="27" fill="#5f8a2a"/>
        <path d="M5 11 Q13.5 4 22 11 L19 13 L17 10.5 Q13.5 9 10 10.5 L8 13 Z" fill="#fff"/>
        <rect x="7" y="14" width="13" height="8" rx="1.5" fill="#fff"/>
        <circle cx="13.5" cy="18" r="2" fill="#5f8a2a"/>
      </svg>
    </div>
  </div>

  <div class="contact contact--right">
    <div class="contact-line">
      <svg class="icon" viewBox="0 0 27 27" aria-hidden="true">
        <rect width="27" height="27" fill="#5f8a2a"/>
        <circle cx="13.5" cy="13.5" r="8" fill="none" stroke="#fff" stroke-width="2"/>
        <ellipse cx="13.5" cy="13.5" rx="3.5" ry="8" fill="none" stroke="#fff" stroke-width="1.5"/>
        <line x1="5.5" y1="13.5" x2="21.5" y2="13.5" stroke="#fff" stroke-width="1.5"/>
      </svg>
      <span>www.velomarquin.com</span>
    </div>
    <div class="contact-line">
      <svg class="icon" viewBox="0 0 27 27" aria-hidden="true">
        <rect width="27" height="27" fill="#5f8a2a"/>
        <rect x="6" y="8" width="15" height="11" fill="none" stroke="#fff" stroke-width="2"/>
        <path d="M6 8 L13.5 14 L21 8" fill="none" stroke="#fff" stroke-width="2"/>
      </svg>
      <span>omarsh@velomarquin.com</span>
    </div>
  </div>
</section>

</body>
</html>
```